Pawn & Gun store business card design

Hello! We would like a new business card design for our pawn & gun store. We loan money on items of value and sell firearms, jewelry, electronics & more.

Card will need to have the following information:

Business name - Prairie Nickel Pawn & Gun
Address - 2417 Hwy 41 S. Suite B Cedar Hollow, OK 73061
Employees name - Marcus Pellen
Phone number - 972-555-0183
Email - PrairieNickelPawn@mailhaven.example
Website - PrairieNickelPawn.example

Somewhere on the card we would like it to say "Offering 10 Month Layaway!" & "We buy & loan on anything of value!". Our main store color is orange (please see logo). Logo does not have to be on the business card but it can be. Would like the back to have an area to write a note on the back. We like vintage things like old coins, collectables, firearms and more so think about this in the design. We want a business card as unique as our store!

Colors

Designer to choose colors to be used in the design.

Requirements
Nice to have
• Vintage Style

```html
<!DOCTYPE html>
<html lang="en">
<head>
<meta charset="utf-8">
<title>Prairie Nickel Pawn &amp; Gun – Business Card</title>
<link href="https://fonts.googleapis.com/css2?family=Lato:wght@400;700&display=swap" rel="stylesheet">
<style>
  :root {
    --backdrop: #5c5c5c;
    --card-orange: #d95f27;
    --ink-dark: #3a2216;
    --ink-light: #ffffff;
    --rule: rgba(255, 220, 200, 0.55);
    --ghost: rgba(200, 80, 25, 0.6);
  }
  html, body {
    margin: 0;
    padding: 0;
    width: 1200px;
    height: 960px;
    overflow: hidden;
    background: var(--backdrop);
    font-family: "Lato", sans-serif;
  }
  .card {
    position: absolute;
    top: 177px;
    width: 364px;
    height: 637px;
    background: var(--card-orange);
    border-radius: 22px;
    box-shadow: 0 10px 18px rgba(0, 0, 0, 0.28);
    overflow: hidden;
  }
  .card--front { left: 168px; }
  .card--back { left: 662px; }

  .line-text {
    position: absolute;
    left: 0;
    width: 100%;
    text-align: center;
    margin: 0;
    white-space: nowrap;
  }
  .brand-name {
    top: 150px;
    font-size: 32px;
    font-weight: 700;
    line-height: 1.1;
    color: var(--ink-light);
  }
  .brand-name--ghost {
    top: 222px;
    font-size: 40px;
    line-height: 1.1;
    color: var(--ghost);
  }
  .employee-name {
    top: 364px;
    font-size: 28px;
    font-weight: 700;
    letter-spacing: 1px;
    color: var(--ink-light);
  }
  .contact-icons {
    position: absolute;
    top: 412px;
    left: 0;
    width: 100%;
    height: 26px;
  }
  .rule {
    position: absolute;
    height: 1px;
    background: var(--rule);
  }
  .rule--icons { top: 425px; left: 89px; width: 186px; }
  .rule--lower { top: 532px; left: 88px; width: 188px; }
  .rule--back { top: 532px; left: 40px; width: 284px; }
  .contact-detail {
    font-size: 17px;
    color: var(--ink-dark);
  }
  .contact-email { font-size: 16px; }
  .contact-phone { top: 445px; }
  .contact-email { top: 471px; }
  .contact-web { top: 495px; }
  .address {
    top: 551px;
    font-size: 17px;
    line-height: 21px;
    color: var(--ink-dark);
  }
  .offer {
    top: 455px;
    font-size: 16.5px;
    line-height: 21px;
    color: var(--ink-dark);
  }
  .store-name {
    top: 546px;
    font-size: 24px;
    font-weight: 700;
    color: var(--ink-light);
  }
</style>
</head>
<body>

<section class="card card--front" aria-label="Business card front">
  <p class="line-text brand-name">Prairie Nickel<br>Pawn</p>

  <h1 class="line-text employee-name">MARCUS&nbsp; PELLEN</h1>

  <div class="rule rule--icons"></div>
  <svg class="contact-icons" viewBox="0 0 364 26" aria-hidden="true">
    <g stroke="var(--ink-light)" stroke-width="2" fill="var(--ink-light)">
      <circle cx="161" cy="13" r="10"/>
      <circle cx="182" cy="13" r="10"/>
      <circle cx="203" cy="13" r="10"/>
    </g>
    <path d="M156 8 q1 -1 2 0 l1.5 2.5 -1.3 1.2 q1.2 2.6 3.6 3.6 l1.2 -1.3 2.5 1.5 q1 1 0 2 q-2 2 -5 0 q-3 -2 -5 -5 q-2 -3 0.5 -4.5z" fill="var(--card-orange)"/>
    <rect x="176" y="8.5" width="12" height="9" fill="none" stroke="var(--card-orange)" stroke-width="1.6"/>
    <path d="M176 8.5 l6 5 6 -5" fill="none" stroke="var(--card-orange)" stroke-width="1.6"/>
    <g fill="none" stroke="var(--card-orange)" stroke-width="1.4">
      <circle cx="203" cy="13" r="6.5"/>
      <ellipse cx="203" cy="13" rx="2.8" ry="6.5"/>
      <path d="M196.5 13 h13 M197.5 9.5 h11 M197.5 16.5 h11"/>
    </g>
  </svg>

  <p class="line-text contact-detail contact-phone">972-555-0183</p>
  <p class="line-text contact-detail contact-email">PrairieNickelPawn@mailhaven.example</p>
  <p class="line-text contact-detail contact-web">PrairieNickelPawn.example</p>

  <div class="rule rule--lower"></div>

  <p class="line-text address">Address - 2417 Hwy 41 S.<br>Suite B Cedar Hollow, OK 73061</p>
</section>

<section class="card card--back" aria-label="Business card back">
  <p class="line-text brand-name brand-name--ghost" aria-hidden="true">Prairie Nickel<br>Pawn</p>

  <p class="line-text offer">Offering 10 Month Layaway!<br>&amp;<br>We buy &amp; loan on anything of value!</p>

  <div class="rule rule--back"></div>

  <p class="line-text store-name">Prairie Nickel Pawn &amp; Gun</p>
</section>

</body>
</html>
```